Professional website for psychological services

Create a professional, easy to navigate website using soothing coastal images and incorporate company logo in design. Website is for a small private clinic that provides psychological services and must be appealing to professional men and women. A website I really like is www.velmorlodge.example I would love something like similar.

Target Market(s)

Professional men and women seeking psychological services

Industry/Entity Type

Mental Health

Number of Pages Required

5+ page

Requirements
Must have
• The website must incorporate the logo provided. The name of the company/website is Brindle Oak Wellness Aftercare. Colors must compliment the logo, must be coastal and soothing yet very professional. I would like a website like www.velmorlodge.example
• Pages will be:Home, Services, FAQ and Contact Us. The images included of the building and office are for the contact us page. Under the tab Servies: Individual Psychotherapy, Family Therapy, EMDR I will provide specific content for each.
Nice to have
• I want the website to be easy to navigate and the font easy to read. The writing on the logo is very light and I'm open to changing it slightly if it will be better aesthetically.
Should not have
• Please no pictures of any swimsuits, alcoholic beverages, etc. This is a professional psychological clinic.

```html
<!DOCTYPE html>
<html lang="en">
<head>
<meta charset="utf-8">
<title>Brindle Oak Wellness Aftercare</title>
<link href="https://fonts.googleapis.com/css2?family=Source+Sans+Pro:wght@300;400;600&display=swap" rel="stylesheet">
<style>
  :root{
    --teal:#1fb3cc;
    --teal-deep:#14a3bd;
    --ink:#1d2430;
    --muted:#5d6470;
    --panel:rgba(255,255,255,0.55);
    --band:rgba(255,255,255,0.35);
    --footer:#eef0f4;
    --sea-top:#8fc7ea;
    --sea-mid:#1f7fb0;
    --sea-deep:#0e6f9a;
    --cliff:#7a8b5a;
  }
  *{box-sizing:border-box;margin:0;padding:0}
  html,body{width:1200px;height:2723px;overflow:hidden}
  body{position:relative;background:#fff;font-family:"Source Sans Pro",Arial,sans-serif;color:var(--ink)}
  .abs{position:absolute}

  /* header */
  .site-header{left:0;top:0;width:1200px;height:158px;background:#fff}
  .brand{left:0;width:1200px;text-align:center;color:var(--teal)}
  .brand-mark{display:block;width:22px;height:22px;border-radius:50%;background:var(--teal);margin:0 auto 6px}
  .brand-name{font-size:34px;font-weight:400;line-height:1}
  .brand-sub{font-size:9px;letter-spacing:1px;margin-top:5px}
  .main-nav{left:0;top:124px;width:1200px;height:20px;font-size:13px}
  .main-nav a{position:absolute;top:0;color:var(--ink);text-decoration:none;transform:translateX(-50%)}
  .main-nav a.is-active{color:var(--teal)}
  .main-nav span{position:absolute;top:0}

  /* hero / page background */
  .coast-backdrop{left:0;top:158px;width:1200px;height:2356px;
    background:linear-gradient(180deg,var(--sea-top) 0%,#5aa7d4 8%,var(--sea-mid) 16%,#2a98c0 30%,#7ec4dc 33%,#8cc8e8 38%,#2590bd 48%,#3aa6c8 70%,#4b8f6a 96%,#3e6b3a 100%)}
  .coast-cliff{right:0;top:158px;width:260px;height:2356px;
    background:linear-gradient(90deg,rgba(122,139,90,0) 0%,rgba(122,139,90,0.55) 40%,rgba(160,150,110,0.7) 100%)}

  .portrait-frame{left:194px;top:229px;width:318px;height:350px;background:var(--teal);opacity:.92;padding:14px}
  .portrait-frame .photo{width:100%;height:100%;background:linear-gradient(160deg,#4f7a3c,#c9a58f 55%,#1e2230)}
  .video-card{left:630px;top:227px;width:386px;height:194px;background:#fff;padding:8px}
  .video-card .photo{position:relative;width:100%;height:100%;background:linear-gradient(180deg,#3ec6e0,#1aa9c9 60%,#e6eef2)}
  .play-btn{position:absolute;left:50%;top:50%;width:62px;height:62px;margin:-31px 0 0 -31px;border-radius:50%;background:rgba(255,255,255,.8)}
  .play-btn svg{position:absolute;left:22px;top:17px}
  .quote-card{left:630px;top:448px;width:386px;height:126px;background:rgba(255,255,255,.82);padding:16px 16px;font-size:11.5px;line-height:17px;color:var(--ink)}
  .quote-sign{position:absolute;right:22px;bottom:10px;font-size:18px;font-weight:600}

  .gallery-band{left:0;top:673px;width:1200px;height:262px;background:var(--band)}
  .gallery-item{top:710px;height:167px}
  .g1{left:0;width:296px;background:linear-gradient(180deg,#a8b6cf,#e1dde3 55%,#7d8aa5)}
  .g2{left:301px;width:296px;background:linear-gradient(120deg,#e9e6e1,#d4cbc2 50%,#8b8f99)}
  .g3{left:603px;width:295px;background:linear-gradient(180deg,#5d6e8e,#e7a465 55%,#c7a27f)}
  .g4{left:904px;width:296px;background:linear-gradient(180deg,#d9b24a,#2fb6c8 55%,#9fc7c9)}
  .slider-dots{left:548px;top:897px;display:flex;gap:7px}
  .slider-dots i{width:14px;height:14px;border-radius:50%;background:#fff;display:block}
  .slider-dots i.is-current{background:var(--teal)}

  /* content panel */
  .content-panel{left:151px;top:1006px;width:898px;height:1453px;background:var(--panel)}
  .section-title{font-size:27px;font-weight:400;letter-spacing:.3px;color:var(--ink);text-transform:uppercase}
  .section-copy{width:372px;font-size:11.8px;line-height:19px;color:var(--ink)}
  .section-copy p+p{margin-top:19px}
  .btn{display:block;width:98px;height:29px;line-height:29px;background:var(--teal);color:#fff;font-size:11px;text-align:center;text-transform:uppercase;text-decoration:none}
  .round-photo{width:256px;height:256px;border-radius:50%;border:8px solid #4fc2d8}
  .rp1{left:634px;top:1061px;background:linear-gradient(160deg,#f3f1ec,#2b9fc4 55%,#e8eef0)}
  .rp2{left:181px;top:1406px;background:linear-gradient(140deg,#e9ddd3,#d8b9a6 50%,#f2f2f2)}
  .rp3{left:634px;top:1751px;background:linear-gradient(150deg,#d9c44a,#eae6df 45%,#6d5443)}
  .rp4{left:181px;top:2123px;background:linear-gradient(180deg,#d7e6ee,#7a6a56 55%,#5a7a3c)}

  .contact-form{left:559px;top:2142px;width:457px;height:268px;background:rgba(255,255,255,.6);padding:0 24px}
  .field{position:absolute;font-size:10px;color:var(--ink);border-bottom:1px solid #333;padding-bottom:8px}

  /* footer */
  .site-footer{left:0;top:2514px;width:1200px;height:209px;background:var(--footer)}
  .social{left:0;top:2632px;width:1200px;display:flex;justify-content:center;gap:13px}
  .social i{display:block;width:26px;height:26px;border-radius:50%;background:#1b1b1b}
  .copyright{left:0;top:2676px;width:1200px;text-align:center;font-size:10px;color:var(--ink)}
</style>
</head>
<body>

<header class="site-header abs">
  <div class="brand abs" style="top:22px">
    <span class="brand-mark"></span>
    <div class="brand-name">Brindle Oak</div>
    <div class="brand-sub">WELLNESS AFTERCARE</div>
  </div>
  <nav class="main-nav abs">
    <a class="is-active" style="left:423px" href="#">HOME</a>
    <span style="left:473px">|</span>
    <a style="left:535px" href="#">SERVICES</a>
    <span style="left:594px">|</span>
    <a style="left:639px" href="#">FAQ</a>
    <span style="left:684px">|</span>
    <a style="left:755px" href="#">CONTACT US</a>
  </nav>
</header>

<div class="coast-backdrop abs" role="img" aria-label="Coastal photograph of turquoise sea, sky and green cliffs"></div>
<div class="coast-cliff abs"></div>

<section class="hero">
  <div class="portrait-frame abs"><div class="photo" role="img" aria-label="Portrait photograph of the clinic's therapist"></div></div>
  <div class="video-card abs">
    <div class="photo" role="img" aria-label="Video still of a woman with raised arms by the sea">
      <span class="play-btn"><svg width="22" height="28" viewBox="0 0 22 28"><path d="M0 0L22 14L0 28Z" fill="#1fb3cc"/></svg></span>
    </div>
  </div>
  <blockquote class="quote-card abs">
    "Maecenas dictum pellentesque nisi, non faucibus leo lacinia sit amet. Aenean ut diam nec ante aliquet sodales ut et arcu. Pellentesque sed purus eros. Phasellus molestie massa ut felis luctus finibus."
    <span class="quote-sign">Brindle Oak</span>
  </blockquote>
</section>

<section class="gallery">
  <div class="gallery-band abs"></div>
  <div class="gallery-item g1 abs" role="img" aria-label="Photo of a person on a jetty over a calm lake"></div>
  <div class="gallery-item g2 abs" role="img" aria-label="Photo of a counselling session in an office"></div>
  <div class="gallery-item g3 abs" role="img" aria-label="Photo of a person meditating on a beach at sunset"></div>
  <div class="gallery-item g4 abs" role="img" aria-label="Photo of a person relaxing on a terrace above the sea"></div>
  <div class="slider-dots abs"><i class="is-current"></i><i></i><i></i><i></i><i></i></div>
</section>

<main>
  <div class="content-panel abs"></div>

  <h2 class="section-title abs" style="left:180px;top:1046px">Welcome to Brindle Oak</h2>
  <div class="section-copy abs" style="left:180px;top:1100px">
    <p>Maecenas elementum ac est at convallis. Curabitur orci quam, luctus at pharetra ac, dictum at diam. Mauris posuere turpis vel ligula convallis dapibus. Nullam pharetra, felis sed maximus lacinia, ligula turpis semper arcu, eu pretium eros libero id leo. Nam sagittis nibh at nulla egestas ullam-corper. Vestibulum quis quam erat.</p>
    <p>Maecenas non fermentum ligula, quis fermentum massa. Duis at eros dui. Orci varius natoque penatibus et magnis dis parturient montes, nascetur ridiculus mus. Nulla facilisi.</p>
  </div>
  <a class="btn abs" style="left:180px;top:1283px" href="#">Learn more</a>
  <div class="round-photo rp1 abs" role="img" aria-label="Photo of a woman in a sun hat on a boat"></div>

  <h2 class="section-title abs" style="left:584px;top:1391px">Our Therapies</h2>
  <div class="section-copy abs" style="left:584px;top:1445px">
    <p>Maecenas elementum ac est at convallis. Curabitur orci quam, luctus at pharetra ac, dictum at diam. Mauris posuere turpis vel ligula convallis dapibus. Nullam pharetra, felis sed maximus lacinia, ligula turpis semper arcu, eu pretium eros libero id leo. Nam sagittis nibh at nulla egestas ullam-corper. Vestibulum quis quam erat.</p>
    <p>Maecenas non fermentum ligula, quis fermentum massa. Duis at eros dui. Orci varius natoque penatibus et magnis dis parturient montes, nascetur ridiculus mus. Nulla facilisi.</p>
  </div>
  <a class="btn abs" style="left:584px;top:1627px" href="#">Learn more</a>
  <div class="round-photo rp2 abs" role="img" aria-label="Photo of hands held in comfort"></div>

  <h2 class="section-title abs" style="left:180px;top:1735px">In the Press</h2>
  <div class="section-copy abs" style="left:180px;top:1789px">
    <p>Maecenas elementum ac est at convallis. Curabitur orci quam, luctus at pharetra ac, dictum at diam. Mauris posuere turpis vel ligula convallis dapibus. Nullam pharetra, felis sed maximus lacinia, ligula turpis semper arcu, eu pretium eros libero id leo. Nam sagittis nibh at nulla egestas ullam-corper. Vestibulum quis quam erat.</p>
    <p>Maecenas non fermentum ligula, quis fermentum massa. Duis at eros dui. Orci varius natoque penatibus et magnis dis parturient montes, nascetur ridiculus mus. Nulla facilisi.</p>
  </div>
  <a class="btn abs" style="left:180px;top:1971px" href="#">Learn more</a>
  <div class="round-photo rp3 abs" role="img" aria-label="Photo of a person reading a health magazine beside a laptop and coffee"></div>

  <h2 class="section-title abs" style="left:584px;top:2079px">Contact Us</h2>
  <form class="contact-form abs">
    <span class="field" style="left:24px;top:32px;width:172px">Your Name</span>
    <span class="field" style="left:264px;top:32px;width:172px">Your Email</span>
    <span class="field" style="left:24px;top:96px;width:412px;height:74px">Your Message</span>
    <a class="btn" style="position:absolute;left:24px;top:210px" href="#">Learn more</a>
  </form>
  <div class="round-photo rp4 abs" role="img" aria-label="Photo of the clinic building with palm trees and a fountain"></div>
</main>

<footer class="site-footer abs">
  <div class="brand abs" style="top:24px">
    <span class="brand-mark"></span>
    <div class="brand-name">Brindle Oak</div>
  </div>
</footer>
<div class="social abs" aria-label="Social links"><i></i><i></i><i></i><i></i><i></i></div>
<p class="copyright abs">©2019 By Brindle Oak. All Rights Reserved.</p>

</body>
</html>
```